New Wix Website Design Project For New Finance Company

Create new design for a new page. Website should match existing theme of presentation deck, business card and logo attached to the brief. The site will have five pages

1) Home
2) Investment Criteria
3) Approach
4) Team
5) Contact

Some examples include
http://www.bluemaplefunds.com/

Although not a requirement, if the below white fence or similar could be added subtly to the sight as well, that would be great.

https://www.searvok.com/search?q=white+fence+horse&rlz=7K4TTPM_enUS218US264&source=lnms&tbm=isch&sa=X&ved=0bhVKEwqxmbtnyLvgBhWE3oNKHVtsBF4Q_BUIDyhD&biw=1920&bih=958#imgrc=vkd2PQx47eMLTA:

Target Market(s)

Business Professionals

Font styles to use
Sans Serif

Colors

Designer to choose colors to be used in the design.

Requirements
Must have
• Clean layout. Easy to upload header and footer.

```html
<!DOCTYPE html>
<html lang="en">
<head>
<meta charset="utf-8">
<title>Stone Meadow Capital</title>
<link rel="stylesheet" href="https://fonts.googleapis.com/css2?family=Raleway:wght@300;400;500;600;700;800&family=Roboto:wght@400;500&display=swap">
<style>
:root{
  --blue:#0d5bb5;
  --blue-deep:#0c3a78;
  --blue-light:#4fa3ec;
  --ink:#2b2b2b;
  --grey:#6a6a6a;
  --heading-light:#5a5a5a;
  --white:#ffffff;
}
*{margin:0;padding:0;box-sizing:border-box}
html,body{width:1200px;height:3352px;overflow:hidden}
body{position:relative;background:var(--white);font-family:'Roboto',sans-serif;color:var(--ink)}
.abs{position:absolute}
.brand{font-family:'Raleway',sans-serif;font-weight:700;color:var(--blue);letter-spacing:1px;text-transform:uppercase;white-space:nowrap}

/* header */
.site-header{left:0;top:0;width:1200px;height:112px;background:var(--white)}
.header-brand{left:94px;top:44px;font-size:20px}
.nav-link{top:45px;font-family:'Raleway',sans-serif;font-size:18px;color:var(--ink);white-space:nowrap}
.nav-link.active{color:var(--blue)}

/* hero */
.hero{left:0;top:112px;width:1200px;height:576px;background:linear-gradient(100deg,#1f3347 0%,#4a6278 40%,#8fa3a6 65%,#6f8a5c 100%)}
.hero-title{left:0;top:288px;width:1200px;text-align:center;color:var(--white);font-family:'Raleway',sans-serif;font-weight:700;font-size:72px;letter-spacing:3px;text-transform:uppercase;line-height:1;white-space:nowrap}
.hero-sub{left:0;top:380px;width:1200px;text-align:center;color:var(--white);font-family:'Raleway',sans-serif;font-weight:600;font-size:30px;letter-spacing:10px;text-transform:uppercase;line-height:1}
.hero-tag{left:0;top:446px;width:1200px;text-align:center;color:var(--white);font-family:'Raleway',sans-serif;font-weight:600;font-size:29px;text-transform:uppercase;line-height:1}
.slider-dots{display:flex;gap:8px}
.slider-dots i{width:8px;height:8px;border-radius:50%;background:#fff;display:block}

.v-line{width:3px;background:var(--blue-deep);left:599px}

.section-title{left:0;width:1200px;text-align:center;font-family:'Raleway',sans-serif;font-size:56px;color:var(--heading-light);font-weight:300;line-height:1.2}
.section-title strong{color:var(--blue);font-weight:800}
.section-title.small{font-size:40px}

.btn{display:flex;align-items:center;justify-content:center;border-radius:22px;color:var(--white);font-family:'Raleway',sans-serif;font-weight:600;font-size:17px;background:linear-gradient(90deg,var(--blue) 0%,var(--blue-light) 100%)}

/* about */
.about-frame{left:112px;top:894px;width:368px;height:315px;border:3px solid var(--blue)}
.about-photo{left:139px;top:939px;width:391px;height:335px;background:linear-gradient(180deg,#0f1c35 0%,#2b4b6e 40%,#3f7a3a 62%,#5ea34a 100%)}
.about-text{left:590px;top:966px;width:498px;font-size:14px;line-height:27.6px;color:var(--ink);text-align:justify}
.read-more{left:590px;top:1209px;width:156px;height:43px}

/* what we do */
.services{left:0;top:1397px;width:1200px;height:704px;background:linear-gradient(180deg,#f2f3f5 0%,#e4e7ea 60%,#dfe2e5 100%)}
.service{width:260px;text-align:center}
.service-icon{width:112px;height:112px;margin:0 auto;border-radius:50%;background:var(--white);box-shadow:0 4px 14px rgba(13,91,181,.25);display:flex;align-items:center;justify-content:center}
.service h3{margin-top:36px;font-family:'Raleway',sans-serif;font-weight:500;font-size:22px;color:var(--ink)}
.service p{margin-top:12px;font-size:16px;line-height:25px;color:var(--grey)}
.view-more{left:521px;top:1965px;width:156px;height:44px}

/* testimonials */
.testimonials{left:0;top:2101px;width:1200px;height:541px;background:#f7f8fa}
.desk-photo{left:490px;top:2101px;width:710px;height:541px;background:linear-gradient(90deg,#f7f8fa 0%,#eceef0 55%,#d8dadd 100%)}
.quote{left:250px;top:2368px;width:700px;text-align:center;font-size:15.5px;line-height:28px;color:var(--ink)}
.quote-author{left:0;top:2474px;width:1200px;text-align:center;font-family:'Raleway',sans-serif;font-size:22px;color:var(--ink)}
.testimonials-dots{left:580px;top:2537px}
.testimonials-dots i{background:var(--blue-deep);width:6px;height:6px}
.arrow{top:2388px}

/* solutions */
.solutions{left:0;top:2642px;width:1200px;height:480px;background:linear-gradient(90deg,#bfc3c8 0%,#eceef0 22%,#f5f6f7 50%,#eceef0 78%,#bfc3c8 100%)}
.solutions-text{left:260px;top:2846px;width:680px;text-align:center;font-size:16px;line-height:29px;color:var(--ink)}
.quote-btn{left:496px;top:2973px;width:206px;height:42px}

/* footer */
.site-footer{left:0;top:3122px;width:1200px;height:230px;background:var(--blue-deep)}
.footer-brand{left:92px;top:3192px;font-size:20px;color:var(--white)}
.footer-divider{width:2px;height:85px;top:3158px;background:rgba(255,255,255,.6)}
.footer-col{text-align:center;color:var(--white);font-size:16px;line-height:35px}
.copyright{left:0;top:3287px;width:1200px;text-align:center;color:var(--white);font-size:16px}
</style>
</head>
<body>

<header class="site-header abs"></header>
<div class="brand header-brand abs">Stone Meadow Capital</div>
<nav>
  <span class="nav-link active abs" style="left:507px">Home</span>
  <span class="nav-link abs" style="left:608px">Investment Criteria</span>
  <span class="nav-link abs" style="left:813px">Approach</span>
  <span class="nav-link abs" style="left:946px">Team</span>
  <span class="nav-link abs" style="left:1043px">Contact</span>
</nav>

<section class="hero abs" role="img" aria-label="City street lined with glass office towers and green trees"></section>
<div class="hero-title abs">Stone Meadow</div>
<div class="hero-sub abs">Capital</div>
<div class="hero-tag abs">A New Finance Company</div>
<div class="slider-dots abs" style="left:583px;top:651px"><i></i><i></i><i></i></div>

<div class="v-line abs" style="top:688px;height:67px"></div>

<h2 class="section-title abs" style="top:782px"><strong>ABOUT</strong> US</h2>
<div class="about-frame abs"></div>
<div class="about-photo abs" role="img" aria-label="White wooden fence along a green pasture at dusk"></div>
<p class="about-text abs">The point of using Lorem Ipsum is that it has a more-or-less normal distribution of letters, as opposed to using 'Content here, content here', making it look like readable English. Many desktop publishing packages and web page editors now use Lorem Ipsum as their default model text, and a search for 'lorem ipsum' will uncover many web sites still in their infancy. The point of using Lorem Ipsum is that it has a more-or-less normal distribution of letters, as opposed to using 'Content here, content here', making it look like readable English. Many desktop publishing packages</p>
<div class="btn read-more abs">Read More</div>

<section class="services abs" role="img" aria-label="Faded skyline of office towers"></section>
<div class="v-line abs" style="top:1397px;height:89px"></div>
<h2 class="section-title abs" style="top:1511px"><strong>WHAT</strong>&nbsp; WE DO</h2>

<div class="service abs" style="left:69px;top:1665px">
  <div class="service-icon"><svg width="56" height="56" viewBox="0 0 56 56" fill="none" stroke="#0d5bb5" stroke-width="2.5"><rect x="8" y="14" width="40" height="26" rx="2"/><path d="M4 44h48M16 22h24M16 28h24M16 34h14"/></svg></div>
  <h3>Investment</h3>
  <p>It is a long established fact that a reader will be distracted</p>
</div>
<div class="service abs" style="left:337px;top:1665px">
  <div class="service-icon"><svg width="56" height="56" viewBox="0 0 56 56" fill="none" stroke="#0d5bb5" stroke-width="2.5"><circle cx="18" cy="14" r="5"/><circle cx="38" cy="14" r="5"/><path d="M10 30c0-6 4-9 8-9s8 3 8 9M30 30c0-6 4-9 8-9s8 3 8 9M6 34h44M14 34v14M42 34v14"/></svg></div>
  <h3>Approach</h3>
  <p>It is a long established fact that a reader will be distracted</p>
</div>
<div class="service abs" style="left:623px;top:1665px">
  <div class="service-icon"><svg width="56" height="56" viewBox="0 0 56 56" fill="none" stroke="#0d5bb5" stroke-width="2.5"><circle cx="30" cy="16" r="9"/><path d="M30 12v8M6 38h10l8 4h12l12-8-4-3-10 5H26M16 34h10"/></svg></div>
  <h3>Finance</h3>
  <p>It is a long established fact that a reader will be distracted</p>
</div>
<div class="service abs" style="left:882px;top:1665px">
  <div class="service-icon"><svg width="56" height="56" viewBox="0 0 56 56" fill="none" stroke="#0d5bb5" stroke-width="2.5"><rect x="12" y="10" width="28" height="38" rx="2"/><path d="M20 8h12v6H20zM18 24h16M18 30h16M18 36h8M36 44l12-14 4 4-12 14z"/></svg></div>
  <h3>Business Services</h3>
  <p>It is a long established fact that a reader will be distracted</p>
</div>
<div class="btn view-more abs">View More</div>

<section class="testimonials abs"></section>
<div class="desk-photo abs" role="img" aria-label="White desk with a coffee cup, glasses and a pen"></div>
<div class="v-line abs" style="top:2101px;height:89px"></div>
<h2 class="section-title small abs" style="top:2263px"><strong>TESTIMONIALS</strong></h2>
<svg class="arrow abs" style="left:136px" width="28" height="60" viewBox="0 0 28 60" fill="none" stroke="#333" stroke-width="2.5"><path d="M26 2L2 30l24 28"/></svg>
<svg class="arrow abs" style="left:1036px" width="28" height="60" viewBox="0 0 28 60" fill="none" stroke="#333" stroke-width="2.5"><path d="M2 2l24 28L2 58"/></svg>
<p class="quote abs">It is a long established fact that a reader will be distracted by the readable content of a page when looking at its layout. The point of using Lorem Ipsum is that it has a more-or-less normal distribution of letters, as opposed to using 'Content here, content here', making</p>
<div class="quote-author abs">- Porro quisquam</div>
<div class="slider-dots testimonials-dots abs"><i></i><i></i><i></i></div>

<section class="solutions abs" role="img" aria-label="Looking up between tall glass office towers"></section>
<div class="v-line abs" style="top:2642px;height:56px"></div>
<h2 class="section-title abs" style="top:2764px;font-size:46px"><strong>OUR</strong> SOLUTIONS</h2>
<p class="solutions-text abs">The point of using Lorem Ipsum is that it has a more-or-less normal distribution of letters, as opposed to using 'Content here, content here', making it look like readable English. Many desktop publishing packages and web page editors</p>
<div class="btn quote-btn abs">Get a Quote Now</div>

<footer class="site-footer abs"></footer>
<div class="brand footer-brand abs">Stone Meadow Capital</div>
<div class="footer-divider abs" style="left:426px"></div>
<div class="footer-col abs" style="left:460px;top:3160px;width:280px">214 Harlow Lane<br>Fairbrook, CA 94021</div>
<div class="footer-divider abs" style="left:759px"></div>
<div class="footer-col abs" style="left:790px;top:3157px;width:270px">Tel: 555-014-2290<br>Email : info@stonemeadow.com</div>
<div class="copyright abs">© Copyright 2019 . All Rights Reserved.</div>

</body>
</html>
```